Meadowline Lawncare by RT

Design a eye catching EDDM postcard for Lawn Care business... 6.5" x 8" EDDM Postcards with required bleed points

There are a few EDDM rules to follow which are.

1. Be sure to add your Postal Indicia it needs to read
“PRST STD ECRWSS U.S. POSTAGE PAID EDDM RETAIL”
in the top right area of your EDDM Flyer Postcard

2. The address area also needs to be filled in with
“****ECRWSS**** Local Postal Customer”

3. Both of these items need to be present on the same side for example both on the back of your EDDM mailer.
Please see the image on the side here for a visual description on how to set up your EDDM mailer correctly. (Attached Sample Template)

Target Market(s)

Home Owners that has a Lawn Care need

Industry/Entity Type

Lawn Care

Font styles to use
Serif

Colors

Designer to choose colors to be used in the design.

Requirements
Must have
• A beautiful background that capture the homeowner eyes when they open their mailbox and see this small card.
• My number: 409-555-0173
• My Name & Email: Dorian Pelham - dopeturfworks@mailcrest.net

```html
<!DOCTYPE html>
<html lang="en">
<head>
<meta charset="utf-8">
<title>Meadowline Lawncare by RT – EDDM Postcard</title>
<link rel="stylesheet" href="https://fonts.googleapis.com/css2?family=Montserrat:wght@500;600;700;800&display=swap">
<style>
  :root {
    --stage: #2b3232;
    --paper: #fbfcfa;
    --ink: #1f1f1f;
    --forest: #2f4a22;
    --deep: #24391b;
    --lime: #5ce12b;
    --leaf: #3fae1c;
    --grass-dark: #2f8f14;
    --phone: #2c8a12;
    --indicia-line: #6b2a2a;
    --address-line: #9aa3a3;
  }
  * { margin: 0; padding: 0; box-sizing: border-box; }
  html, body { width: 1200px; height: 1045px; overflow: hidden; background: var(--stage); }
  body { font-family: "Montserrat", sans-serif; color: var(--ink); position: relative; }

  .postcard {
    position: absolute; left: 16px; top: 47px;
    width: 1298px; height: 1057px;
    transform: scale(0.9); transform-origin: top left;
    background: var(--paper); overflow: hidden;
  }
  .abs { position: absolute; }

  .top-bands { left: 0; top: 0; width: 1298px; height: 16px; }

  .brand { left: 44px; top: 80px; display: flex; align-items: center; gap: 20px; }
  .brand-dot { width: 34px; height: 34px; border-radius: 50%; background: var(--lime); }
  .brand-name { font-weight: 800; font-size: 50px; line-height: 1.05; color: var(--ink); letter-spacing: 1px; }

  .contact { left: 600px; top: 38px; }
  .contact-name { font-weight: 500; font-size: 34px; margin-left: 47px; color: #333; }
  .contact-row { display: flex; align-items: center; gap: 12px; }
  .contact-phone { font-weight: 800; font-size: 56px; color: var(--phone); letter-spacing: 0.5px; line-height: 1.1; }
  .contact-email { font-weight: 500; font-size: 27px; }

  .indicia {
    width: 116px; border: 2px solid var(--indicia-line); background: #fff;
    font-weight: 600; font-size: 14px; line-height: 18px; text-align: center; padding: 11px 2px;
  }
  .address {
    width: 309px; height: 90px; border: 2px solid var(--address-line); background: #fff;
    font-weight: 500; font-size: 18px; line-height: 24px; padding: 14px 10px;
  }
  .address .stars { text-align: right; font-size: 16px; margin-right: 14px; }

  .grass { left: 0; width: 1298px; }
  .grass-top { top: 200px; height: 100px; background: linear-gradient(#f4fbef 0%, #7fd84f 45%, var(--grass-dark) 100%); }
  .grass-bottom { top: 960px; height: 97px; background: linear-gradient(#eefbe6 0%, #79dc3e 35%, var(--grass-dark) 100%); }

  .photos { left: 0; top: 295px; width: 1298px; height: 432px; }

  .services-tab { left: 0; top: 740px; width: 330px; height: 72px; }
  .services-title { left: 62px; top: 750px; font-weight: 800; font-size: 41px; color: #fff; }

  .service-list { list-style: none; }
  .service-list li { display: flex; align-items: center; gap: 14px; height: 41.5px; font-weight: 600; font-size: 30px; }
  .tick { width: 26px; height: 26px; flex: none; }
</style>
</head>
<body>
<main class="postcard">
  <svg class="abs top-bands" viewBox="0 0 1298 16" aria-hidden="true">
    <polygon points="0,0 360,0 344,16 0,16" fill="var(--forest)"/>
    <polygon points="376,0 1298,0 1298,16 360,16" fill="var(--lime)"/>
  </svg>

  <div class="abs grass grass-top" role="img" aria-label="Band of tall green grass"></div>

  <div class="abs brand">
    <span class="brand-name">MEADOWLINE<br>Lawncare</span>
    <span class="brand-dot"></span>
  </div>

  <div class="abs contact">
    <div class="contact-name">Dorian Pelham</div>
    <div class="contact-row">
      <svg width="34" height="34" viewBox="0 0 34 34" aria-hidden="true">
        <circle cx="17" cy="17" r="15" fill="none" stroke="var(--phone)" stroke-width="2.5"/>
        <path d="M12 9c1-1 2-1 3 0l2 3c.5 1 0 2-1 2.5 .5 2 2 3.5 4 4 .5-1 1.5-1.5 2.5-1l3 2c1 1 1 2 0 3-4 3-13-6-13.5-13z" fill="var(--phone)"/>
      </svg>
      <span class="contact-phone">409-555-0173</span>
    </div>
    <div class="contact-row">
      <svg width="34" height="34" viewBox="0 0 34 34" aria-hidden="true">
        <circle cx="17" cy="17" r="15" fill="none" stroke="var(--phone)" stroke-width="2.5"/>
        <rect x="9" y="11" width="16" height="12" rx="1" fill="var(--phone)"/>
        <path d="M9.5 11.5 17 18l7.5-6.5" fill="none" stroke="#fff" stroke-width="1.5"/>
      </svg>
      <span class="contact-email">dopeturfworks@mailcrest.net</span>
    </div>
  </div>

  <div class="abs indicia" style="left:1130px; top:44px;">PRST STD<br>ECRWSS<br>U.S. POSTAGE<br>PAID<br>EDDM RETAIL</div>
  <div class="abs address" style="left:936px; top:170px;">
    <div class="stars">***************ECRWSS*****</div>
    Local<br>Postal Customer
  </div>

  <svg class="abs photos" viewBox="0 0 1298 432">
    <rect x="0" y="0" width="1298" height="432" fill="var(--deep)"/>
    <polygon points="0,0 755,0 665,415 0,415" fill="#8fb070" role="img" aria-label="Photo of a two-storey house with trimmed hedges and mulched front garden"/>
    <polygon points="755,0 1235,0 1200,238 720,238" fill="#6fbf3d" role="img" aria-label="Photo of a backyard lawn with stepping-stone path and wooden fence"/>
    <polygon points="710,255 940,255 915,413 680,413" fill="#5fae33" role="img" aria-label="Photo of a red lawn mower cutting grass"/>
    <polygon points="958,255 1183,255 1158,413 930,413" fill="#7c9a6a" role="img" aria-label="Photo of a newly landscaped front yard"/>
    <polygon points="1255,0 1298,0 1298,413 1175,413" fill="var(--lime)"/>
  </svg>

  <svg class="abs services-tab" viewBox="0 0 330 72" aria-hidden="true">
    <polygon points="0,0 330,0 300,72 0,72" fill="var(--leaf)"/>
    <polygon points="0,0 312,0 282,64 0,64" fill="var(--forest)"/>
  </svg>
  <div class="abs services-title">SERVICES</div>

  <ul class="abs service-list" style="left:50px; top:821px;">
    <li><svg class="tick" viewBox="0 0 26 26" aria-hidden="true"><circle cx="13" cy="13" r="13" fill="var(--lime)"/><path d="M7 13.5l4 4 8-9" fill="none" stroke="#fff" stroke-width="3"/></svg>Weekly Lawn Maintenance</li>
    <li><svg class="tick" viewBox="0 0 26 26" aria-hidden="true"><circle cx="13" cy="13" r="13" fill="var(--lime)"/><path d="M7 13.5l4 4 8-9" fill="none" stroke="#fff" stroke-width="3"/></svg>Landscape Installation</li>
    <li><svg class="tick" viewBox="0 0 26 26" aria-hidden="true"><circle cx="13" cy="13" r="13" fill="var(--lime)"/><path d="M7 13.5l4 4 8-9" fill="none" stroke="#fff" stroke-width="3"/></svg>Irrigation System</li>
  </ul>
  <ul class="abs service-list" style="left:557px; top:821px;">
    <li><svg class="tick" viewBox="0 0 26 26" aria-hidden="true"><circle cx="13" cy="13" r="13" fill="var(--lime)"/><path d="M7 13.5l4 4 8-9" fill="none" stroke="#fff" stroke-width="3"/></svg>Weekly Lawn Maintenance</li>
    <li><svg class="tick" viewBox="0 0 26 26" aria-hidden="true"><circle cx="13" cy="13" r="13" fill="var(--lime)"/><path d="M7 13.5l4 4 8-9" fill="none" stroke="#fff" stroke-width="3"/></svg>Landscape Installation</li>
    <li><svg class="tick" viewBox="0 0 26 26" aria-hidden="true"><circle cx="13" cy="13" r="13" fill="var(--lime)"/><path d="M7 13.5l4 4 8-9" fill="none" stroke="#fff" stroke-width="3"/></svg>Irrigation System</li>
  </ul>

  <div class="abs grass grass-bottom" role="img" aria-label="Green grass strip with a small figure mowing the lawn"></div>

  <div class="abs indicia" style="left:1128px; top:785px;">PRST STD<br>ECRWSS<br>U.S. POSTAGE<br>PAID<br>EDDM RETAIL</div>
  <div class="abs address" style="left:927px; top:914px;">
    <div class="stars">***************ECRWSS*****</div>
    Local<br>Postal Customer
  </div>
</main>
</body>
</html>
```